Business card alterations

I have changed my business name from Orvan Laser Rejuvenation Clinic to simply "Orvan Laser Clinic' and need this logo changed to reflect same

Orvan Laser Clinic
Est. 2004

I also need new business cards with above logo included and this attached card changed to the following.
Marguerite Halcombe
Dermal Aesthetician
Grad Cert in Laser & IPL Treatments

I need at least one logo in less than 4mb so I can upload into my newsletter format so I can upload to newsletters, emails etc

Thanks
Marg

Industry/Entity Type

Business

```html
<!DOCTYPE html>
<html lang="en">
<head>
<meta charset="utf-8">
<title>Orvan Laser Clinic – Business Card</title>
<link rel="stylesheet" href="https://fonts.googleapis.com/css2?family=Open+Sans:wght@400;600;700&family=Arimo:wght@400;700&display=swap">
<style>
  :root {
    --page-bg: #f2f2f2;
    --card-green: #00a054;
    --ink-white: #ffffff;
    --card-shadow: rgba(0, 0, 0, 0.18);
  }
  * { box-sizing: border-box; margin: 0; padding: 0; }
  html, body {
    width: 1200px;
    height: 900px;
    overflow: hidden;
    background: var(--page-bg);
  }
  .canvas {
    position: relative;
    width: 1200px;
    height: 900px;
  }
  .card {
    position: absolute;
    left: 110px;
    top: 150px;
    width: 980px;
    height: 600px;
    background: var(--card-green);
    border-radius: 38px;
    box-shadow: 0 18px 40px var(--card-shadow);
    color: var(--ink-white);
  }
  .card__frame {
    position: absolute;
    inset: 16px;
    border: 6px solid var(--ink-white);
    border-radius: 28px;
  }
  .brand {
    position: absolute;
    left: 0;
    right: 0;
    top: 48px;
    text-align: center;
  }
  .brand__name {
    font-family: "Open Sans", sans-serif;
    font-weight: 600;
    font-size: 168px;
    line-height: 1;
    letter-spacing: -2px;
  }
  .brand__clinic {
    margin-top: 34px;
    font-family: "Open Sans", sans-serif;
    font-weight: 700;
    font-size: 26px;
    letter-spacing: 13px;
    text-indent: 13px;
  }
  .brand__est {
    margin-top: 8px;
    font-family: "Open Sans", sans-serif;
    font-weight: 400;
    font-size: 22px;
    letter-spacing: 7px;
    text-indent: 7px;
  }
  .person {
    position: absolute;
    right: 510px;
    top: 390px;
    text-align: right;
    font-family: "Open Sans", sans-serif;
  }
  .person__name {
    font-weight: 600;
    font-size: 33px;
    line-height: 1.2;
  }
  .person__role {
    font-size: 19px;
    line-height: 1.35;
    margin-top: 2px;
  }
  .divider {
    position: absolute;
    left: 488px;
    top: 386px;
    width: 2px;
    height: 170px;
    background: var(--ink-white);
  }
  .contact {
    position: absolute;
    left: 512px;
    top: 388px;
    font-family: "Arimo", sans-serif;
    font-size: 21px;
    line-height: 1.3;
    list-style: none;
  }
  .contact li { margin-bottom: 10px; }
  .contact__phone { font-weight: 700; }
  .contact__address { margin-bottom: 0; }
</style>
</head>
<body>
<main class="canvas">
  <section class="card" aria-label="Orvan Laser Clinic business card">
    <div class="card__frame"></div>

    <header class="brand">
      <div class="brand__name">Orvan</div>
      <div class="brand__clinic">ORVAN LASER CLINIC</div>
      <div class="brand__est">EST. 2004</div>
    </header>

    <div class="person">
      <div class="person__name">Marguerite Halcombe</div>
      <div class="person__role">Dermal Aesthetician</div>
      <div class="person__role">Grad Cert in Laser &amp; IPL Treatments</div>
    </div>

    <div class="divider"></div>

    <ul class="contact">
      <li class="contact__phone">T (08) 7420 3185</li>
      <li>info@orvanclinic.com.au</li>
      <li>www.orvanclinic.com.au</li>
      <li class="contact__address">58 Ashwood Terrace<br>Kelvale SA 5072</li>
    </ul>
  </section>
</main>
</body>
</html>
```